Summer Sale Graphics for Social Media

I want to create 11 social media graphics (new Instagram size 4:5 (1080 x 1350 pixels) focusing on our Summer Sale Graphics, using any of the pics attached. Use the attached pics, NO RANDOM STOCK PHOTOGRAPHY. For the color scheme of the graphics, they should all be complementary to the product colors in the photos.
You can add any of the photos attached but none are required. You can do some of the graphics in all text. I mainly need BOLD text that says one of the headlines (11 total) SEE ATTACHED WORD DOCUMENT for the headlines to use.

```html
<!DOCTYPE html>
<html lang="en">
<head>
<meta charset="utf-8">
<title>Summer Sale Social Graphics</title>
<link href="https://fonts.googleapis.com/css2?family=Anton&family=Archivo+Black&family=Alfa+Slab+One&family=Oswald:wght@600;700&family=Lobster&display=swap" rel="stylesheet">
<style>
:root{
  --board:#2b2a2b;
  --teal:#1796b4;
  --coral:#f8836f;
  --pink:#f66d85;
  --purple:#8b3fe0;
  --violet:#a44cf0;
  --yellow:#fbd66c;
  --blue:#0b88d8;
  --sky:#5db9d7;
  --orange:#f57c3b;
  --magenta:#e15bb6;
  --navy:#1c2b78;
  --cream:#fdf2e3;
  --white:#ffffff;
  --ink:#1b1b1b;
  --skin:linear-gradient(180deg,#3a2a26 0%,#8a5b46 30%,#f1eeee 55%,#e6e2e2 75%,#2a2a2a 100%);
  --bottles:linear-gradient(90deg,#f4f1f4,#e7e2ea 25%,#f4f1f4 50%,#e7e2ea 75%,#f4f1f4);
}
*{margin:0;padding:0;box-sizing:border-box}
html,body{width:747px;height:1200px;overflow:hidden;background:var(--board)}
.board{position:relative;width:747px;height:1200px}
.tile{position:absolute;width:223px;height:279px;overflow:hidden}
.tile>svg.waves{position:absolute;inset:0;width:100%;height:100%}
.abs{position:absolute;white-space:nowrap}
.photo{position:absolute;background:var(--skin);border-radius:40px 40px 6px 6px}
.bottles{position:absolute;background:var(--bottles);border-radius:8px 8px 4px 4px}
.h-black{font-family:"Archivo Black",sans-serif;line-height:.92;color:var(--white)}
.h-cond{font-family:"Anton",sans-serif;line-height:1;color:var(--white)}
.h-slab{font-family:"Alfa Slab One",serif;line-height:1}
.h-osw{font-family:"Oswald",sans-serif;font-weight:700;line-height:1}
.disc{position:absolute;border-radius:50%;display:flex;flex-direction:column;align-items:center;justify-content:center;font-family:"Anton",sans-serif;line-height:1.05;text-align:center}
.r1{top:22px}.r2{top:315px}.r3{top:607px}.r4{top:899px}
.c1{left:20px}.c2{left:262px}.c3{left:504px}
</style>
</head>
<body>
<main class="board">

<section class="tile r1 c1" style="background:var(--teal)">
  <svg class="waves" viewBox="0 0 223 279"><path d="M30 140 C30 80 80 60 140 70 C190 78 210 60 223 55 L223 279 L30 279 Z" fill="var(--coral)"/><path d="M0 250 C60 235 140 270 223 255 L223 279 L0 279Z" fill="var(--teal)"/></svg>
  <div class="photo" role="img" aria-label="Smiling woman in white crop top presenting supplements" style="left:22px;top:65px;width:120px;height:180px"></div>
  <div class="bottles" role="img" aria-label="Row of supplement bottles on marble counter" style="left:6px;top:228px;width:150px;height:42px"></div>
  <h1 class="abs h-black" style="left:12px;top:10px;font-size:22.5px">GET SNATCHED<br>FOR SUMMER</h1>
  <div class="abs h-black" style="right:8px;top:84px;font-size:12.5px">SUPPLEMENTS</div>
  <div class="abs h-black" style="right:10px;top:102px;font-size:28px;text-align:right">ON<br>SALE<br>NOW!</div>
  <div class="abs h-black" style="left:160px;top:198px;width:58px;height:81px;background:var(--pink);border-radius:10px 10px 0 0;font-size:15px;padding:10px 0 0 8px">UP TO<br><span style="font-size:24px">$15</span><br><span style="font-size:20px">OFF</span></div>
</section>

<section class="tile r1 c2" style="background:var(--purple)">
  <svg class="waves" viewBox="0 0 223 279"><path d="M0 120 C70 90 150 110 223 95 L223 200 L0 200Z" fill="var(--yellow)"/><path d="M0 150 C60 135 120 170 223 145 L223 230 L0 240Z" fill="var(--magenta)"/><path d="M0 215 C80 200 160 215 223 205 L223 279 L0 279Z" fill="var(--violet)"/></svg>
  <div class="abs h-cond" style="left:0;width:223px;top:6px;text-align:center;font-size:33px">LIMITED-TIME</div>
  <div class="abs h-cond" style="left:0;width:223px;top:38px;text-align:center;font-size:40px">SUMMER SALE</div>
  <div class="abs h-cond" style="left:0;width:223px;top:80px;text-align:center;font-size:22px">SNATCH YOUR</div>
  <div class="bottles" role="img" aria-label="Four supplement bottles in a row" style="left:12px;top:110px;width:198px;height:110px"></div>
  <div class="disc" style="left:8px;top:210px;width:52px;height:52px;background:var(--blue);color:var(--white);font-size:13px">Up to<br>$15 OFF</div>
  <div class="abs h-black" style="right:6px;top:228px;font-size:17px;text-align:center">SUPPLEMENTS<br><span style="font-size:25px">NOW!</span></div>
</section>

<section class="tile r1 c3" style="background:var(--yellow)">
  <svg class="waves" viewBox="0 0 223 279"><rect width="223" height="84" fill="var(--teal)"/><path d="M60 180 L223 180 L223 279 L60 279Z" fill="#eceaea"/></svg>
  <div class="photo" role="img" aria-label="Smiling woman in white crop top" style="left:108px;top:40px;width:112px;height:195px"></div>
  <div class="bottles" role="img" aria-label="Supplement bottles on marble counter" style="left:78px;top:190px;width:142px;height:70px"></div>
  <div class="abs h-black" style="left:12px;top:10px;font-size:19.5px;letter-spacing:-.3px;color:var(--pink)">SUMMER'S HERE</div>
  <div class="abs h-black" style="left:13px;top:40px;font-size:17px;line-height:1.08">AND WE'RE<br><span style="font-size:15px">HAVING THE</span></div>
  <div class="abs h-cond" style="left:13px;top:90px;font-size:30px;color:var(--teal);line-height:.95">BIGGEST<br><span style="font-size:20px">SALE OF THE</span><br>YEAR</div>
  <div class="abs h-black" style="left:15px;top:180px;width:61px;height:99px;background:var(--purple);border-radius:6px 6px 0 0;font-size:15px;padding:14px 0 0 10px">UP TO<br><span style="font-size:24px">$15</span><br><span style="font-size:22px">OFF</span></div>
</section>

<section class="tile r2 c1" style="background:var(--purple)">
  <svg class="waves" viewBox="0 0 223 279"><path d="M0 185 C60 180 110 200 150 220 L223 200 L223 279 L0 279Z" fill="var(--yellow)"/><path d="M170 70 C200 60 215 80 223 90 L223 210 L150 220Z" fill="var(--yellow)"/><path d="M90 279 C120 240 180 220 223 210 L223 279Z" fill="var(--blue)"/></svg>
  <div class="photo" role="img" aria-label="Smiling woman holding a supplement bottle" style="left:105px;top:55px;width:112px;height:180px"></div>
  <div class="bottles" role="img" aria-label="Four supplement bottles" style="left:100px;top:215px;width:115px;height:56px"></div>
  <div class="abs h-cond" style="left:0;width:223px;top:8px;font-size:17px;color:var(--yellow);text-align:center;line-height:1.1">SLIM WAIST. FLAT TUMMY.<br>MORE ENERGY.</div>
  <div class="abs h-slab" style="left:14px;top:52px;font-size:20px;color:var(--white);line-height:1.2">MORE<br>ENERGY.<br>LET'S GO!</div>
  <div class="abs h-black" style="left:12px;top:132px;font-size:29px;color:var(--yellow)">SALE<br>NOW!</div>
  <div class="abs h-black" style="left:22px;top:200px;font-size:14px;color:var(--ink)">UP TO<br><span style="font-size:24px">$15</span><br><span style="font-size:22px">OFF</span></div>
</section>

<section class="tile r2 c2" style="background:var(--yellow)">
  <svg class="waves" viewBox="0 0 223 279"><path d="M0 0 H223 V80 C150 95 70 70 0 85Z" fill="var(--purple)"/><path d="M0 180 C70 165 150 185 223 170 L223 279 L0 279Z" fill="var(--blue)"/></svg>
  <h2 class="abs h-osw" style="left:0;width:223px;top:12px;text-align:center;font-size:21px;color:var(--white);line-height:1.08">DETOX, BURN FAT,<br>AND TURN HEADS<br><span style="font-size:19px">THIS SUMMER</span></h2>
  <div class="bottles" role="img" aria-label="Four supplement bottles" style="left:15px;top:100px;width:198px;height:90px"></div>
  <div class="abs h-black" style="left:26px;top:202px;font-size:32px">SALE<br>NOW!</div>
  <div class="disc" style="left:142px;top:212px;width:54px;height:54px;background:var(--white);color:var(--ink);font-size:13px">Up to<br>$15 OFF</div>
</section>

<section class="tile r2 c3" style="background:var(--yellow)">
  <svg class="waves" viewBox="0 0 223 279"><path d="M0 40 C80 20 150 60 223 20 L223 120 C140 150 60 100 0 130Z" fill="#f9b04c"/><path d="M110 60 C150 20 200 40 223 10 L223 279 L120 279Z" fill="var(--sky)"/><path d="M0 200 C60 210 120 250 223 205 L223 279 L0 279Z" fill="var(--orange)"/></svg>
  <div class="photo" role="img" aria-label="Smiling woman holding a supplement bottle" style="left:10px;top:18px;width:145px;height:261px;border-radius:60px 60px 0 0"></div>
  <div class="abs h-black" style="right:6px;top:10px;font-size:28px">FINAL</div>
  <div class="abs h-black" style="right:6px;top:38px;font-size:14px">COUNTDOWN</div>
  <div class="abs h-cond" style="left:165px;top:55px;font-size:38px;writing-mode:vertical-rl;color:var(--white);text-shadow:-2px 0 0 var(--blue)">TO SUMMER</div>
  <div class="abs" style="left:12px;top:212px;font-family:'Lobster',cursive;font-size:30px;color:var(--white);line-height:1">Sale</div>
  <div class="abs h-black" style="left:12px;top:246px;font-size:22px">NOW!</div>
  <div class="disc" style="left:172px;top:225px;width:46px;height:46px;background:#fbc24f;color:var(--ink);font-size:11px">Up to<br>$15 OFF</div>
</section>

<section class="tile r3 c1" style="background:var(--yellow)">
  <svg class="waves" viewBox="0 0 223 279"><path d="M0 0 H223 V75 C150 95 70 95 0 75Z" fill="var(--pink)"/><path d="M0 190 C70 180 150 185 223 180 L223 279 L0 279Z" fill="var(--purple)"/></svg>
  <h2 class="abs h-cond" style="left:0;width:223px;top:12px;text-align:center;font-size:32px;line-height:1.02">SUMMER ISN'T<br>WAITING</h2>
  <div class="abs h-osw" style="left:0;width:223px;top:90px;text-align:center;font-size:19px;color:var(--ink)">NEITHER SHOULD YOU</div>
  <div class="bottles" role="img" aria-label="Four supplement bottles" style="left:22px;top:112px;width:178px;height:85px"></div>
  <div class="abs h-black" style="left:34px;top:202px;font-size:31px;text-align:center">SALE<br>NOW!</div>
  <div class="abs h-black" style="left:152px;top:202px;font-size:15px;color:var(--yellow)">UP TO<br><span style="font-size:25px">$15</span><br><span style="font-size:22px">OFF</span></div>
</section>

<section class="tile r3 c2" style="background:var(--blue)">
  <svg class="waves" viewBox="0 0 223 279"><path d="M0 30 C60 20 90 60 130 90 C170 120 200 140 223 130 L223 180 C160 200 100 150 0 150Z" fill="var(--sky)"/><path d="M0 120 C40 140 60 220 150 205 C190 200 210 190 223 195 L223 279 L0 279Z" fill="var(--yellow)"/></svg>
  <div class="photo" role="img" aria-label="Smiling woman in brown top holding supplement bottles" style="left:22px;top:8px;width:108px;height:205px;background:linear-gradient(180deg,#2e211d,#8b5d47 30%,#9a6a55 60%,#1c1c1c)"></div>
  <div class="bottles" role="img" aria-label="Four supplement bottles" style="left:10px;top:205px;width:135px;height:66px"></div>
  <div class="abs h-black" style="left:125px;top:18px;font-size:22px">One<br>Sale.<br>One<br>Body.</div>
  <div class="abs h-black" style="right:12px;top:133px;font-size:21px;text-align:right">One<br><span style="text-shadow:1px 1px 0 var(--blue)">Summer</span><br>to Slay</div>
  <div class="disc" style="left:160px;top:210px;width:54px;height:54px;background:var(--white);color:var(--ink);font-size:13px">Up to<br>$15 OFF</div>
</section>

<section class="tile r3 c3" style="background:var(--yellow)">
  <svg class="waves" viewBox="0 0 223 279"><path d="M100 279 V130 A62 62 0 0 1 223 130 V279Z" fill="var(--cream)"/><path d="M0 210 C80 215 150 250 223 225 L223 279 L0 279Z" fill="var(--teal)"/></svg>
  <div class="photo" role="img" aria-label="Smiling woman in brown top holding supplement bottles" style="left:102px;top:70px;width:115px;height:170px;background:linear-gradient(180deg,#2e211d,#8b5d47 30%,#9a6a55 60%,#1c1c1c)"></div>
  <div class="bottles" role="img" aria-label="Four supplement bottles" style="left:8px;top:214px;width:108px;height:60px"></div>
  <h2 class="abs h-slab" style="left:12px;top:8px;font-size:20px;color:var(--teal);line-height:1.1">Your Summer<br>Body Won't Wait</h2>
  <div class="abs h-black" style="left:12px;top:72px;font-size:32px;color:var(--teal)">SALE<br><span style="font-size:22px">NOW!</span></div>
  <div class="abs h-black" style="left:16px;top:140px;font-size:14px;color:var(--ink)">UP TO<br><span style="font-size:25px">$15</span><br><span style="font-size:22px">OFF</span></div>
</section>

<section class="tile r4 c1" style="background:var(--sky)">
  <svg class="waves" viewBox="0 0 223 279"><path d="M0 0 H223 V55 C150 70 70 55 0 70Z" fill="var(--teal)"/><path d="M0 240 C80 220 150 240 223 225 L223 279 L0 279Z" fill="var(--navy)"/></svg>
  <div class="photo" role="img" aria-label="Smiling woman in white crop top presenting supplements" style="left:68px;top:65px;width:100px;height:175px"></div>
  <div class="bottles" role="img" aria-label="Supplement bottles on counter" style="left:40px;top:225px;width:145px;height:40px"></div>
  <h2 class="abs h-black" style="left:0;width:223px;top:10px;text-align:center;font-size:36px">HURRY!</h2>
  <div class="abs h-black" style="left:0;width:223px;top:48px;text-align:center;font-size:16px">OUR SUMMER SLIM</div>
  <div class="abs h-black" style="left:12px;top:102px;font-size:18px">Down<br>Sale Is<br>On</div>
  <div class="abs h-black" style="right:6px;top:148px;font-size:18px">Don't<br>Miss It!</div>
  <div class="disc" style="left:12px;top:165px;width:48px;height:48px;background:var(--navy);color:var(--white);font-size:11px">Up to<br>$15 OFF</div>
</section>

<section class="tile r4 c2" style="background:var(--magenta)">
  <svg class="waves" viewBox="0 0 223 279"><path d="M110 120 C150 120 190 90 223 80 L223 279 L110 279Z" fill="var(--yellow)"/><path d="M120 140 C160 130 200 110 223 110 L223 279 L120 279Z" fill="var(--violet)"/><path d="M0 190 C60 180 110 200 170 200 L223 210 L223 279 L0 279Z" fill="var(--purple)"/></svg>
  <div class="photo" role="img" aria-label="Smiling woman holding a supplement bottle" style="left:10px;top:8px;width:140px;height:195px"></div>
  <div class="bottles" role="img" aria-label="Four supplement bottles" style="left:100px;top:212px;width:115px;height:58px"></div>
  <h2 class="abs h-black" style="right:8px;top:18px;font-size:26px">SALE:<br>YOUR<br><span style="font-size:16px">SUMMER</span></h2>
  <div class="abs h-black" style="left:168px;top:138px;font-size:14px">UP TO<br><span style="font-size:24px">$15</span><br><span style="font-size:22px">OFF</span></div>
  <div class="abs h-black" style="left:12px;top:210px;font-size:22px">Body<br>Starts<br>Here</div>
</section>

</main>
</body>
</html>
```